Upsell Vertical Banner Ad Design For B2B Marketing Agency Vertical 768px × 1180px IS THE SIZE

I need a banner made for my website www.brightlanepromotionhub.biz This banner will be an upsell advertisement for after someone signs up for my monthly program. When they login to their account for the 1st time I will give them the chance to upgrade their account to our annual program with just one click.

this is a page that upsells it currently to give you an idea how we market ourselves:
https://tlpx.pagevault-example.com/page/tlp-annual-upsell

Use this content:

Are You Ready To Commit To Taking Your Business To The Next Level?

Because We're In This For The Long-Haul and Dedicated To Your Success...

Save $300 By Upgrading To An Annual Membership And Pay Only $74/mth

((BUTTON))Yes, Upgrade My Plan Right Now!

*Must prepay the full year at only $898/yr!

Target Market(s)

business owners

Industry/Entity Type

Marketing

Requirements
Must have
• 768px × 1180px IS THE SIZE vertical

Use this content:

Nice to have
• Use this content:

Should not have
• Use this content:

```html
<!DOCTYPE html>
<html lang="en">
<head>
<meta charset="utf-8">
<title>Annual Membership Upgrade Banner</title>
<link href="https://fonts.googleapis.com/css2?family=Lato:wght@400;700;900&display=swap" rel="stylesheet">
<style>
  :root {
    --blue-deep: #2b7be0;
    --blue-light: #4d9af1;
    --white: #ffffff;
    --ink: #2a2a2a;
    --orange: #f5831f;
    --illustration-blue: #8fb8f5;
    --illustration-navy: #3f5fc8;
    --rocket-orange: #e9772a;
  }
  * { margin: 0; padding: 0; box-sizing: border-box; }
  html, body { width: 781px; height: 1200px; overflow: hidden; background: var(--white); }
  .banner {
    position: relative;
    width: 781px;
    height: 1200px;
    overflow: hidden;
    background: var(--blue-deep);
    font-family: 'Lato', sans-serif;
  }
  .banner__backdrop { position: absolute; inset: 0; width: 781px; height: 1200px; }
  .headline {
    position: absolute;
    left: 68px;
    top: 52px;
    color: var(--white);
    font-size: 39px;
    font-weight: 400;
    line-height: 49px;
    letter-spacing: 5px;
    white-space: nowrap;
    z-index: 2;
  }
  .headline strong { font-weight: 700; }
  .scene-art {
    position: absolute;
    left: 410px;
    top: 70px;
    width: 335px;
    height: 480px;
    border-radius: 24px;
    background: linear-gradient(160deg, var(--illustration-navy) 0%, var(--illustration-blue) 55%, #c9daf9 100%);
    opacity: 0.85;
  }
  .rocket-art {
    position: absolute;
    left: 76px;
    top: 515px;
    width: 145px;
    height: 290px;
    border-radius: 72px 72px 20px 20px;
    background: linear-gradient(180deg, var(--rocket-orange) 0%, #eef3fb 30%, #dfe8f6 75%, #f6c14b 100%);
  }
  .tagline {
    position: absolute;
    left: 230px;
    top: 612px;
    color: var(--white);
    font-size: 28px;
    line-height: 38px;
    letter-spacing: 4.6px;
    white-space: nowrap;
  }
  .offer {
    position: absolute;
    left: 0;
    top: 864px;
    width: 770px;
    text-align: center;
    color: var(--ink);
    font-size: 33px;
    line-height: 44px;
    letter-spacing: 4.6px;
  }
  .offer strong { font-weight: 700; }
  .cta-button {
    position: absolute;
    left: 92px;
    top: 1010px;
    width: 587px;
    height: 115px;
    background: var(--orange);
    color: var(--white);
    display: flex;
    align-items: center;
    justify-content: center;
    text-align: center;
    font-size: 36px;
    font-weight: 700;
    line-height: 43px;
    letter-spacing: 4px;
    text-decoration: none;
  }
  .fine-print {
    position: absolute;
    left: 0;
    top: 1130px;
    width: 770px;
    text-align: center;
    color: var(--ink);
    font-size: 20px;
    letter-spacing: 3.6px;
    white-space: nowrap;
  }
  .fine-print strong { font-weight: 700; }
</style>
</head>
<body>
  <main class="banner">
    <svg class="banner__backdrop" viewBox="0 0 781 1200" aria-hidden="true">
      <path fill="var(--blue-light)" d="M0,0 H560 C470,130 440,300 320,420 C220,520 90,540 0,620 Z"/>
      <path fill="var(--white)" d="M0,905 C30,880 60,868 95,880 C125,830 190,800 260,815 C300,790 350,790 385,812 C420,775 470,770 505,795 C550,770 600,770 630,792 C680,780 740,790 781,825 V1200 H0 Z"/>
    </svg>

    <div class="scene-art" role="img" aria-label="Illustration of two business people at a desk reviewing charts with a growth dashboard screen"></div>
    <div class="rocket-art" role="img" aria-label="Illustration of a launching rocket"></div>

    <h1 class="headline"><strong>Are You Ready</strong><br>To Commit To<br>Taking Your<br>Business To<br><strong>The Next</strong><br><strong>Level?</strong></h1>

    <p class="tagline">Because We're In This For<br>The Long-Haul and Dedicated<br>To Your Success!</p>

    <p class="offer"><strong>Save $300</strong> By Upgrading To<br>An Annual Membership And<br><strong>Pay Only $74/mth</strong></p>

    <a class="cta-button" href="#upgrade">Yes, Upgrade My Plan<br>Right Now!</a>

    <p class="fine-print">*Must prepay the full year at only <strong>$898/yr!</strong></p>
  </main>
</body>
</html>
```